Torvane Facilities Business Card Design

We would now like to design business cards with the new Torvane Facilities logo

Target Market(s)

Professional

Industry/Entity Type

Professional services

Contact Information for Business Card

Employee name, title, phone number, email address, corporate office address and logo.

Font styles to use
Sans Serif

Colors
0054AA
0677BA
7BADD7
CADEEF
E8F1F8

Requirements
Must have
• My logo
Should not have
• any other pictures or images besides my logo

```html
<!DOCTYPE html>
<html lang="en">
<head>
<meta charset="utf-8">
<title>Torvane Facilities – Business Card</title>
<link href="https://fonts.googleapis.com/css2?family=Montserrat:wght@400;500;700;800&display=swap" rel="stylesheet">
<style>
  :root{
    --blue-deep:#0054AA;
    --blue:#3677C0;
    --blue-mid:#7BADD7;
    --blue-pale:#CADEEF;
    --blue-mist:#E8F1F8;
    --white:#FFFFFF;
    --ink:#1A1A1A;
    --shadow-grey:#A9A9A9;
    --page:#2A2B2E;
  }
  *{box-sizing:border-box;margin:0;padding:0}
  html,body{width:1200px;height:900px;overflow:hidden}
  body{
    background:var(--page);
    font-family:"Montserrat",sans-serif;
    display:flex;flex-direction:column;align-items:center;justify-content:center;gap:60px;
  }
  .card{
    position:relative;width:620px;height:354px;border-radius:26px;overflow:hidden;
    box-shadow:0 12px 30px rgba(0,0,0,.45);
  }
  .card--front{background:var(--white)}
  .card--back{background:var(--blue);display:flex;align-items:center;justify-content:center}
  .front-wave{position:absolute;inset:0;width:100%;height:100%}
  .brand{
    position:absolute;left:44px;top:70px;display:flex;align-items:center;gap:14px;
    color:var(--blue);font-weight:800;font-size:30px;line-height:1.05;text-transform:uppercase;letter-spacing:.5px;
  }
  .brand__square{width:44px;height:44px;background:var(--blue);flex:none}
  .divider{position:absolute;left:320px;top:60px;width:2px;height:200px;background:var(--blue)}
  .contact{position:absolute;left:345px;top:64px;color:var(--ink)}
  .contact__name{color:var(--blue);font-weight:800;font-size:19px;text-transform:uppercase;letter-spacing:.3px}
  .contact__title{font-size:14px;font-weight:500;margin-top:2px}
  .contact__address{font-size:13.5px;font-weight:500;line-height:1.35;margin-top:14px}
  .contact__list{list-style:none;margin-top:12px;font-size:13.5px;font-weight:500;line-height:1.45}
  .contact__list li{display:flex;align-items:center;gap:8px}
  .contact__list svg{width:14px;height:14px;flex:none;fill:var(--blue)}
  .back-brand{
    display:flex;align-items:center;gap:22px;color:var(--blue-pale);
    font-weight:800;font-size:52px;line-height:1.05;text-transform:uppercase;letter-spacing:1px;
  }
  .back-brand__square{width:78px;height:78px;background:var(--blue-pale);flex:none}
</style>
</head>
<body>

<section class="card card--front" aria-label="Business card front">
  <svg class="front-wave" viewBox="0 0 620 354" preserveAspectRatio="none" aria-hidden="true">
    <path d="M0,150 C45,150 20,235 190,270 C330,300 430,285 500,354 L0,354 Z" fill="var(--blue)"/>
    <path d="M34,190 C60,240 120,258 200,276 C330,300 430,292 488,346" fill="none" stroke="var(--shadow-grey)" stroke-width="3"/>
    <path d="M28,180 C60,232 120,250 200,268 C330,296 430,290 492,350" fill="none" stroke="var(--white)" stroke-width="3"/>
  </svg>

  <div class="brand">
    <span class="brand__square"></span>
    <span>Torvane<br>Facilities</span>
  </div>

  <div class="divider"></div>

  <div class="contact">
    <p class="contact__name">Dara Whitlock</p>
    <p class="contact__title">Co-Founder</p>
    <p class="contact__address">4180 N. Harbor Lane<br>Suite 212 Kelmont.14</p>
    <ul class="contact__list">
      <li><svg viewBox="0 0 24 24"><path d="M6.6 10.8a15 15 0 0 0 6.6 6.6l2.2-2.2a1 1 0 0 1 1-.25 11.4 11.4 0 0 0 3.6.57 1 1 0 0 1 1 1V20a1 1 0 0 1-1 1A17 17 0 0 1 3 4a1 1 0 0 1 1-1h3.5a1 1 0 0 1 1 1c0 1.25.2 2.45.57 3.6a1 1 0 0 1-.25 1z"/></svg>+254-300-41752</li>
      <li><svg viewBox="0 0 24 24"><path d="M2 5h20v14H2z M2 5l10 8 10-8" /></svg>info@torvanefacilities.com</li>
      <li><svg viewBox="0 0 24 24"><circle cx="12" cy="12" r="10"/></svg>www.torvanefacilities.com</li>
    </ul>
  </div>
</section>

<section class="card card--back" aria-label="Business card back">
  <div class="back-brand">
    <span class="back-brand__square"></span>
    <span>Torvane<br>Facilities</span>
  </div>
</section>

</body>
</html>
```